Stylish, Masculine Design - Men's Clothing

Granary Coat Mart is a 14,000 square foot warehouse outlet store open to the public since 2005. 50+ brands. Well-known designer brand names and private labels. 30-80% off retail everyday. Lowest prices guaranteed. Average suit price $150. Average shirt price $20. One-stop shop shopping. Men's suits, tuxedos, tuxedo rentals, dress shirts, ties, dress shoes, boy's suits and tuxedos, clergy robes, clergy shirts, cologne, loungewear. Slim fits (Prom Dance), business styles, "church" fashion, security-related uniform. Alterations done by expert tailors on premises for an extra charge.
The final design for both business card and logo should portray stylishness and masculinity.
Updates
We will be changing our name. Details below.New name: Warehouse Suit & TuxFormer name: Granary Coat Mart Added Monday, December 26, 2016
Target Market(s)
Gender: 80% Male, 15% Female, 5% Transgender
Location: 80% 10 Mile Radius, 20% >10 Mile Radius
Age: 17-18 (Primarily prom), 18-35 (Primarily Interviews and Weddings), 36-70 (primarily Church and events)
Race: African-American 50%, Latino-American 20%, White 15%, 10% Asian 5% Other
Religions: Christian 50%, 20% Catholic, 10% Mormon, 20% Other/None
Occupation: Local government 40%, Large corporation employee 20%, Small business employee 10%, Small business owner 10%, 20% Unemployed (high school, college)
Education: High School or equivalent 40%, College 30%, Some College 20%, Masters/Doctors 10%
Industry/Entity Type
Retail
Contact Information for Business Card
Name: Peter Olund
Title: Sales Associate
Address: 418 E. Mirabeth Ave. Halden Park, CA 90381
Phone Number: 428.555.0182
Slogan: Warehouse Selection. Outlet Prices, Outstanding Service
www.granarycoatmart.example
Logo Text
GCM (Acronym for Granary Coat Mart) or Image
Requirements
Must have
- Easy to read
- Visually appealing

```html
<!DOCTYPE html>
<html lang="en">
<head>
<meta charset="utf-8">
<title>Granary Coat Mart – Business Card</title>
<link href="https://fonts.googleapis.com/css2?family=Montserrat:wght@300;400;600;700&display=swap" rel="stylesheet">
<style>
  :root {
    --page-bg: #e6e4e2;
    --card-white: #ffffff;
    --ink: #231f20;
    --band-dark: #262324;
    --accent-red: #e3202a;
    --text-light: #f2f2f2;
  }
  * { margin: 0; padding: 0; box-sizing: border-box; }
  html, body {
    width: 1200px; height: 800px; overflow: hidden;
    background: var(--page-bg);
    font-family: "Montserrat", Arial, sans-serif;
  }
  .business-card {
    position: absolute; left: 417px; top: 80px;
    width: 366px; height: 640px;
    background: var(--card-white);
    border-radius: 16px;
    overflow: hidden;
    box-shadow: 0 10px 30px rgba(0,0,0,.18);
  }
  .brand-name {
    position: absolute; left: 0; right: 0; top: 30px;
    text-align: center;
    color: var(--ink);
    font-weight: 700;
    text-transform: uppercase;
    line-height: 1;
  }
  .brand-name .line-top { display: block; font-size: 48px; letter-spacing: 4px; }
  .brand-name .line-bottom { display: block; font-size: 52px; letter-spacing: 1px; margin-top: 8px; }
  .slogan {
    position: absolute; left: 0; right: 0; top: 170px;
    text-align: center;
    font-size: 8px; font-weight: 600;
    color: var(--ink);
    text-transform: uppercase;
    letter-spacing: .4px;
  }
  .tie-emblem {
    position: absolute; left: 170px; top: 215px;
    width: 26px; height: 128px;
    background: var(--accent-red);
  }
  .holder-name {
    position: absolute; left: 0; right: 0; top: 368px;
    text-align: center;
    color: var(--accent-red);
    font-size: 30px; font-weight: 600;
    letter-spacing: 1px;
    line-height: 36px;
    text-transform: uppercase;
  }
  .holder-title {
    position: absolute; left: 0; right: 0; top: 407px;
    text-align: center;
    color: var(--ink);
    font-size: 11px; font-weight: 600;
    letter-spacing: 4.5px;
    line-height: 14px;
    text-transform: uppercase;
  }
  .contact-band {
    position: absolute; left: 0; right: 0; top: 441px; bottom: 0;
    background: var(--band-dark);
    border-top: 3px solid var(--accent-red);
  }
  .contact-row {
    position: absolute; left: 0; right: 0;
    display: flex; align-items: flex-start;
    padding-left: 30px;
    color: var(--text-light);
    font-size: 19px; font-weight: 300;
    line-height: 25px;
  }
  .contact-row.phone { top: 10px; }
  .contact-row.web { top: 64px; font-size: 17.5px; }
  .contact-row.address { top: 118px; }
  .contact-row svg { flex: none; width: 24px; height: 24px; margin: 1px 6px 0 0; }
  .divider {
    position: absolute; left: 0; right: 0; height: 3px;
    background: var(--accent-red);
  }
  .divider.first { top: 48px; }
  .divider.second { top: 102px; }
</style>
</head>
<body>
  <div class="business-card">
    <div class="brand-name">
      <span class="line-top">Granary</span>
      <span class="line-bottom">Coat Mart</span>
    </div>
    <div class="slogan">Wide Selection. Fair Prices. Friendly Service</div>
    <div class="tie-emblem" role="img" aria-label="Red necktie illustration"></div>
    <div class="holder-name">Peter Olund</div>
    <div class="holder-title">Sales Associate</div>

    <div class="contact-band">
      <div class="contact-row phone">
        <svg viewBox="0 0 24 24" aria-hidden="true">
          <circle cx="12" cy="12" r="10.5" fill="none" stroke="#f2f2f2" stroke-width="1.8"/>
          <rect x="8.5" y="5.5" width="7" height="13" rx="1.2" fill="none" stroke="#f2f2f2" stroke-width="1.6"/>
          <line x1="11" y1="16.3" x2="13" y2="16.3" stroke="#f2f2f2" stroke-width="1.4"/>
        </svg>
        <span>428.555.0182</span>
      </div>
      <div class="divider first"></div>
      <div class="contact-row web">
        <svg viewBox="0 0 24 24" aria-hidden="true">
          <circle cx="12" cy="12" r="10.5" fill="none" stroke="#f2f2f2" stroke-width="1.8"/>
          <circle cx="12" cy="12" r="6.5" fill="none" stroke="#f2f2f2" stroke-width="1.4"/>
          <ellipse cx="12" cy="12" rx="3" ry="6.5" fill="none" stroke="#f2f2f2" stroke-width="1.2"/>
          <line x1="5.5" y1="12" x2="18.5" y2="12" stroke="#f2f2f2" stroke-width="1.2"/>
          <line x1="6.5" y1="9" x2="17.5" y2="9" stroke="#f2f2f2" stroke-width="1"/>
          <line x1="6.5" y1="15" x2="17.5" y2="15" stroke="#f2f2f2" stroke-width="1"/>
        </svg>
        <span>www.granarycoatmart.example</span>
      </div>
      <div class="divider second"></div>
      <div class="contact-row address">
        <svg viewBox="0 0 24 24" aria-hidden="true">
          <circle cx="12" cy="12" r="10.5" fill="none" stroke="#f2f2f2" stroke-width="1.8"/>
          <path d="M12 18.5 C9 14.8 7.5 12.5 7.5 10.3 A4.5 4.5 0 0 1 16.5 10.3 C16.5 12.5 15 14.8 12 18.5 Z" fill="none" stroke="#f2f2f2" stroke-width="1.5"/>
          <circle cx="12" cy="10.3" r="1.7" fill="#f2f2f2"/>
        </svg>
        <span>418 E. Mirabeth Ave.<br>Halden Park, CA 90381</span>
      </div>
    </div>
  </div>
</body>
</html>
```